Stationery Design Project

Please create a custom Stationery Design for Brookfern Homes. The logo is attached to this brief.

Please Include:
- Letterhead
- With Compliments slip
- Envelope

Please also see open Business Card project: http://tasks.pixelbazaar-example.com/task.aspx?id=517290

Industry/Entity Type

Business

```html
<!DOCTYPE html>
<html lang="en">
<head>
<meta charset="utf-8">
<title>Brookfern Homes — Stationery</title>
<link href="https://fonts.googleapis.com/css2?family=Open+Sans:wght@400;600;700&display=swap" rel="stylesheet">
<style>
  :root{
    --blue:#0b6fbe;
    --yellow:#f7c500;
    --ink:#4a4a4a;
    --muted:#8a8a8a;
    --paper:#ffffff;
    --backdrop:#ececec;
    --rule:#bdbdbd;
  }
  *{box-sizing:border-box;margin:0;padding:0}
  html,body{width:1200px;height:960px;overflow:hidden}
  body{background:var(--backdrop);font-family:"Open Sans",Arial,sans-serif;color:var(--ink);position:relative}

  .sheet{position:absolute;background:var(--paper);box-shadow:0 4px 14px rgba(0,0,0,.12);overflow:hidden}
  .band{position:absolute;left:0;bottom:0;width:100%;display:block}

  .brand{display:flex;align-items:center;gap:7px;color:var(--blue);font-weight:400;white-space:nowrap}
  .brand-dot{border-radius:50%;background:var(--yellow);flex:none}

  .contact{display:flex;align-items:center;gap:5px;white-space:nowrap}
  .icon{display:inline-block;background:var(--blue);border-radius:2px;flex:none}
  .nowrap p{white-space:nowrap}
  .divider{width:1px;background:var(--rule);align-self:stretch;flex:none}

  /* Letterhead */
  .letterhead{left:440px;top:30px;width:420px;height:594px}
  .letterhead .brand{position:absolute;left:44px;top:46px;font-size:19px}
  .letterhead .brand-dot{width:22px;height:22px}
  .letterhead .footer{position:absolute;left:44px;bottom:124px;display:flex;gap:12px;font-size:8px;line-height:1.7}
  .letterhead .icon{width:8px;height:8px}

  /* Compliments slip */
  .compliments{left:885px;top:300px;width:295px;height:200px}
  .compliments .title{position:absolute;right:22px;top:20px;font-size:15px;color:var(--blue);font-weight:400}
  .compliments .footer{position:absolute;left:20px;top:66px;display:flex;flex-direction:column;gap:8px}
  .compliments .brand{font-size:13px;gap:6px}
  .compliments .brand-dot{width:15px;height:15px}
  .compliments .details{display:flex;gap:9px;font-size:6.5px;line-height:1.7}
  .compliments .icon{width:6px;height:6px}

  /* Envelope */
  .envelope{left:40px;top:650px;width:600px;height:290px}
  .envelope .head{position:absolute;left:28px;top:26px;display:flex;gap:10px;align-items:center;font-size:8px;line-height:1.6}
  .envelope .brand{font-size:18px}
  .envelope .brand-dot{width:20px;height:20px}
  .envelope .window{position:absolute;left:120px;top:100px;width:260px;height:108px;border:1px solid #cfcfcf;border-radius:6px}

  /* Business cards */
  .card{width:340px;height:194px}
  .card-back{left:40px;top:40px}
  .card-front{left:40px;top:256px}
  .card-back .heading{position:absolute;left:20px;top:20px;font-size:12px;font-weight:700;color:var(--blue)}
  .card-back .list{position:absolute;left:20px;top:42px;list-style:none;font-size:7.4px;line-height:1.75}
  .card-back .list li{display:flex;align-items:center;gap:5px}
  .tick{width:8px;height:8px;background:var(--blue);border-radius:1px;display:inline-flex;align-items:center;justify-content:center;flex:none}
  .card-back .contacts{position:absolute;left:20px;top:130px;display:flex;gap:14px;font-size:7.5px;color:var(--blue)}
  .card-back .icon{width:9px;height:9px;display:inline-flex;align-items:center;justify-content:center}
  .card-back .brand-dot.solo{position:absolute;right:22px;top:20px;width:22px;height:22px}
  .card-front .brand{position:absolute;left:20px;top:58px;font-size:15px}
  .card-front .brand-dot{width:18px;height:18px}
  .card-front .person{position:absolute;right:22px;top:20px;text-align:right}
  .person .name{font-size:12px;font-weight:600;color:var(--blue)}
  .person .role{font-size:7.5px;color:var(--muted)}
  .card-front .contacts{position:absolute;left:20px;top:92px;font-size:7px;line-height:1.9}
  .card-front .icon{width:8px;height:8px}
</style>
</head>
<body>

<section class="sheet card card-back" aria-label="Business card reverse">
  <span class="brand-dot solo"></span>
  <h2 class="heading">Real Estate Solutions Company</h2>
  <ul class="list">
    <li><span class="tick"><svg width="6" height="6" viewBox="0 0 6 6"><path d="M1 3l1.4 1.4L5 1.6" stroke="#fff" stroke-width="1" fill="none"/></svg></span>Buy Unwanted, Sell and Rent Residential Property</li>
    <li><span class="tick"><svg width="6" height="6" viewBox="0 0 6 6"><path d="M1 3l1.4 1.4L5 1.6" stroke="#fff" stroke-width="1" fill="none"/></svg></span>Make Cash Offers on Homes in Any Condition</li>
    <li><span class="tick"><svg width="6" height="6" viewBox="0 0 6 6"><path d="M1 3l1.4 1.4L5 1.6" stroke="#fff" stroke-width="1" fill="none"/></svg></span>Sell Properties to Investors</li>
    <li><span class="tick"><svg width="6" height="6" viewBox="0 0 6 6"><path d="M1 3l1.4 1.4L5 1.6" stroke="#fff" stroke-width="1" fill="none"/></svg></span>Solve Complex Real Estate Problems</li>
    <li><span class="tick"><svg width="6" height="6" viewBox="0 0 6 6"><path d="M1 3l1.4 1.4L5 1.6" stroke="#fff" stroke-width="1" fill="none"/></svg></span>Private Money Investment Services</li>
    <li><span class="tick"><svg width="6" height="6" viewBox="0 0 6 6"><path d="M1 3l1.4 1.4L5 1.6" stroke="#fff" stroke-width="1" fill="none"/></svg></span>Pay Cash Instantly for Referrals</li>
  </ul>
  <div class="contacts">
    <span class="contact"><span class="icon"><svg width="6" height="6" viewBox="0 0 6 6"><path d="M1 1h1.3l.5 1.3-.7.5a3 3 0 0 0 1.1 1.1l.5-.7L5 3.7V5C2.8 5 1 3.2 1 1z" fill="#fff"/></svg></span>+1 (555) 410-2286</span>
    <span class="contact"><span class="icon"><svg width="6" height="6" viewBox="0 0 6 6"><circle cx="3" cy="3" r="2.2" stroke="#fff" stroke-width=".7" fill="none"/><path d="M.8 3h4.4M3 .8v4.4" stroke="#fff" stroke-width=".6"/></svg></span>www.brookfernhomes-example.com</span>
  </div>
  <svg class="band" viewBox="0 0 340 44" height="44" preserveAspectRatio="none" aria-hidden="true">
    <path d="M240 16 L340 0 L340 10 Q300 18 268 22 Z" fill="var(--yellow)"/>
    <path d="M0 36 L150 36 Q250 30 340 14 L340 44 L0 44 Z" fill="var(--blue)"/>
  </svg>
</section>

<section class="sheet card card-front" aria-label="Business card front">
  <div class="person">
    <p class="name">Marcus Ellery</p>
    <p class="role">Business Director</p>
  </div>
  <div class="brand"><span class="brand-dot"></span>Brookfern Homes</div>
  <div class="contacts">
    <p class="contact"><span class="icon"></span>+1 (555) 410-2286</p>
    <p class="contact"><span class="icon"></span>hello@brookfernhomes-example.com</p>
    <p class="contact"><span class="icon"></span>www.brookfernhomes-example.com</p>
  </div>
  <svg class="band" viewBox="0 0 340 44" height="44" preserveAspectRatio="none" aria-hidden="true">
    <path d="M240 16 L340 0 L340 10 Q300 18 268 22 Z" fill="var(--yellow)"/>
    <path d="M0 36 L150 36 Q250 30 340 14 L340 44 L0 44 Z" fill="var(--blue)"/>
  </svg>
</section>

<section class="sheet letterhead" aria-label="Letterhead">
  <div class="brand"><span class="brand-dot"></span>Brookfern Homes</div>
  <div class="footer">
    <div class="nowrap">
      <p>12 Ridgeway Court, Suite Line</p>
      <p>Alderbrook Business Park, City Name</p>
    </div>
    <span class="divider"></span>
    <div>
      <p class="contact"><span class="icon"></span>+1 (555) 410-2286</p>
      <p class="contact"><span class="icon"></span>hello@brookfernhomes-example.com</p>
    </div>
  </div>
  <svg class="band" viewBox="0 0 420 110" height="110" preserveAspectRatio="none" aria-hidden="true">
    <path d="M270 48 L420 0 L420 30 Q360 50 318 62 Z" fill="var(--yellow)"/>
    <path d="M0 94 L200 94 Q310 84 420 42 L420 110 L0 110 Z" fill="var(--blue)"/>
  </svg>
</section>

<section class="sheet compliments" aria-label="With compliments slip">
  <h2 class="title">With Compliments</h2>
  <div class="footer">
    <div class="brand"><span class="brand-dot"></span>Brookfern Homes</div>
    <div class="details">
      <div class="nowrap">
        <p>12 Ridgeway Court, Suite Line</p>
        <p>Alderbrook Business Park, City Name</p>
      </div>
      <span class="divider"></span>
      <div>
        <p class="contact"><span class="icon"></span>+1 (555) 410-2286</p>
        <p class="contact"><span class="icon"></span>www.brookfernhomes-example.com</p>
      </div>
    </div>
  </div>
  <svg class="band" viewBox="0 0 295 60" height="60" preserveAspectRatio="none" aria-hidden="true">
    <path d="M195 26 L295 0 L295 15 Q258 26 228 32 Z" fill="var(--yellow)"/>
    <path d="M0 50 L130 50 Q215 45 295 22 L295 60 L0 60 Z" fill="var(--blue)"/>
  </svg>
</section>

<section class="sheet envelope" aria-label="Window envelope">
  <div class="head">
    <div class="brand"><span class="brand-dot"></span>Brookfern Homes</div>
    <span class="divider"></span>
    <div class="nowrap">
      <p>12 Ridgeway Court, Suite Line</p>
      <p>Alderbrook Business Park, City Name</p>
    </div>
  </div>
  <div class="window"></div>
  <svg class="band" viewBox="0 0 600 110" height="110" preserveAspectRatio="none" aria-hidden="true">
    <path d="M400 46 L600 0 L600 28 Q520 48 460 60 Z" fill="var(--yellow)"/>
    <path d="M0 96 L290 96 Q450 86 600 40 L600 110 L0 110 Z" fill="var(--blue)"/>
  </svg>
</section>

</body>
</html>
```